Brova -Letter Head

We are predominantly a residential home builder based in Melbourne, Victoria Australia. We construct houses, apartments, townhouses, multi-unit developments.

The name of the company is "Brova"
My company believes in building unique construction projects mainly residential homes. The target customers are upmarket Melbourne residents/investors.

I want the brand name "Brova" to be part of the logo. There's no need to put the word construction in the logo at this stage.

I would also like some ideas for a slogan. But I would like something unique and different for a slogan not the same old cliche.

Industry/Entity Type

Construction

Requirements
Must have
• I need to be able to print quotes, general letters for customers, print tables and pictures on the letter head. So it must not have too much graphics and should be simple.

```html
<!DOCTYPE html>
<html lang="en">
<head>
<meta charset="utf-8">
<title>Brova – Letterhead</title>
<link rel="stylesheet" href="https://fonts.googleapis.com/css2?family=Questrial&display=swap">
<style>
  :root {
    --canvas-bg: #ececec;
    --paper: #f4f4f4;
    --navy: #393750;
    --sky: #6aaad0;
    --white: #ffffff;
    --faint: #e6e6e6;
    --font-main: "Questrial", "Century Gothic", sans-serif;
  }
  html, body {
    margin: 0;
    padding: 0;
    width: 1200px;
    height: 815px;
    overflow: hidden;
    background: var(--canvas-bg);
    font-family: var(--font-main);
  }
  .canvas {
    position: relative;
    width: 1200px;
    height: 815px;
  }
  .sheet {
    position: absolute;
    top: 70px;
    width: 483px;
    height: 683px;
    overflow: hidden;
  }
  .letterhead { left: 80px; background: var(--paper); }
  .back-cover { left: 638px; background: var(--navy); }

  .letterhead-header {
    position: absolute;
    left: 0; top: 0;
    width: 100%;
    height: 98px;
    background: var(--navy);
  }
  .brand-name {
    position: absolute;
    left: 36px;
    top: 26px;
    margin: 0;
    font-size: 40px;
    font-weight: 400;
    line-height: 1;
    color: var(--sky);
    letter-spacing: 1px;
  }
  .tagline {
    position: absolute;
    left: 211px;
    top: 52px;
    margin: 0;
    font-size: 13px;
    color: var(--white);
    letter-spacing: 0.2px;
  }
  .watermark-name {
    position: absolute;
    left: 0;
    top: 300px;
    width: 100%;
    text-align: center;
    font-size: 120px;
    color: var(--faint);
    line-height: 1;
  }
  .letterhead-footer {
    position: absolute;
    left: 0; bottom: 0;
    width: 100%;
    height: 21px;
    background: var(--sky);
    display: flex;
    align-items: center;
    justify-content: center;
    gap: 10px;
    font-size: 6.5px;
    color: var(--white);
  }
  .contact-item { display: flex; align-items: center; gap: 3px; }
  .contact-icon { width: 7px; height: 7px; }

  .cover-mark {
    position: absolute;
    left: 0;
    top: 300px;
    width: 100%;
    text-align: center;
    font-size: 60px;
    line-height: 1;
    color: var(--sky);
    letter-spacing: 1px;
  }
</style>
</head>
<body>
<main class="canvas">
  <section class="sheet letterhead" aria-label="Letterhead">
    <header class="letterhead-header">
      <h1 class="brand-name">Brova</h1>
      <p class="tagline">We Build With Brovaness And Passion</p>
    </header>
    <div class="watermark-name" aria-hidden="true">Brova</div>
    <footer class="letterhead-footer">
      <span class="contact-item">118 Larkspur Ave, Kew VIC 3101</span>
      <span class="contact-item">
        <svg class="contact-icon" viewBox="0 0 10 10" aria-hidden="true"><circle cx="5" cy="5" r="4.3" fill="none" stroke="#fff" stroke-width="0.9"/><path d="M3.4 2.8l1 1-0.5 0.6a3 3 0 0 0 1.7 1.7l0.6-0.5 1 1-0.8 0.8A4 4 0 0 1 2.6 3.6z" fill="#fff"/></svg>
        03-9400-1172
      </span>
      <span class="contact-item">
        <svg class="contact-icon" viewBox="0 0 10 10" aria-hidden="true"><circle cx="5" cy="5" r="4.3" fill="none" stroke="#fff" stroke-width="0.9"/><rect x="2.8" y="3.4" width="4.4" height="3.2" fill="none" stroke="#fff" stroke-width="0.7"/><path d="M2.8 3.4L5 5.2 7.2 3.4" fill="none" stroke="#fff" stroke-width="0.7"/></svg>
        info@brova.com
      </span>
      <span class="contact-item">
        <svg class="contact-icon" viewBox="0 0 10 10" aria-hidden="true"><circle cx="5" cy="5" r="4.3" fill="none" stroke="#fff" stroke-width="0.9"/><ellipse cx="5" cy="5" rx="1.7" ry="4.3" fill="none" stroke="#fff" stroke-width="0.7"/><path d="M0.7 5h8.6" stroke="#fff" stroke-width="0.7"/></svg>
        www.brova.com
      </span>
    </footer>
  </section>

  <section class="sheet back-cover" aria-label="Letterhead back cover">
    <div class="cover-mark">Brova</div>
  </section>
</main>
</body>
</html>
```